RM Tomás Rivera (Business Card)

Hi designers, in this work, I'm looking for an sophisticated stylish, elegant and proffesional personal card. We have a laboratory of pathology automated, with equipments high quality.
In this web the designers, have created my business logo, the name is "RM Tomás Rivera"
In our lab, we principal work is to prepare the biopsies for further diagnostic of diseases like cancer, tumors, etc.
I need that the first face, only having my complete logo (Rm Tomás Rivera, Laboratorio de procesamiento Histologico)
The overleaf, could repeat the same logo, like water logo.
In this face, I need to say: My full data:

Técnico en Anatomía Patológica
Tomás Rivera Ibarra M.P 47203
Av. Paredes Luján 418 - 2do piso - Instituto Marbel.
Córdoba, Argentina
(0351) 154820937
rivera.tomas@correolab.example

with respect the colors of card, use your imagination, the original logo color is violet, I haven't chosen a color base for the card.

attached pictures are examples of cards I like your DESIGN.
Attached too, the original logo to my company.

the size of card are:
horizontal: 9cm
vertical: 5,5cm

any question that you have, not doubt to question me,
Hand to work!

Industry/Entity Type

Laboratory

Requirements
Must have
• designers sophisticated, not simples, like show the images attached

```html
<!DOCTYPE html>
<html lang="es">
<head>
<meta charset="utf-8">
<title>Tomás Rivera · Tarjeta personal</title>
<link rel="stylesheet" href="https://fonts.googleapis.com/css2?family=Arimo:wght@400;700&family=PT+Sans:wght@400&family=PT+Sans+Narrow:wght@400&display=swap">
<style>
  :root {
    --backdrop: #161617;
    --card-light: #f4f4f4;
    --card-dark: #303031;
    --ink: #333333;
    --ink-soft: #444444;
    --violet: #6a2e91;
    --violet-light: #8a4bb5;
    --band-dark: #262626;
    --grey-mark: #c4c4c4;
    --text-on-dark: #e2e2e2;
  }
  * { margin: 0; padding: 0; box-sizing: border-box; }
  html, body { width: 1200px; height: 900px; overflow: hidden; }
  body { background: var(--backdrop); position: relative; font-family: "PT Sans", sans-serif; }

  .card {
    position: absolute; left: 370px; width: 456px; height: 279px;
    box-shadow: 0 6px 18px rgba(0, 0, 0, 0.55);
    overflow: hidden;
  }

  /* Front face */
  .card-front { top: 161px; background: var(--card-light); }
  .front-mark {
    position: absolute; left: 28px; top: 72px; width: 38px; height: 38px;
    border: 2px solid var(--violet);
  }
  .front-brand {
    position: absolute; left: 76px; top: 81px;
    font-family: "Arimo", sans-serif; font-weight: 700; font-size: 15px;
    color: var(--violet); letter-spacing: 0.3px; white-space: nowrap;
  }
  .holder-name {
    position: absolute; left: 260px; top: 88px;
    font-family: "Arimo", sans-serif; font-weight: 700; font-size: 16.5px; color: var(--ink);
    white-space: nowrap;
  }
  .holder-licence {
    position: absolute; left: 260px; top: 109px;
    font-family: "Arimo", sans-serif; font-size: 12px; color: var(--violet); letter-spacing: 0.4px;
  }
  .holder-address {
    position: absolute; right: 223px; top: 199px; text-align: right;
    font-size: 12px; line-height: 15px; color: var(--ink-soft); white-space: nowrap;
  }
  .contact-divider {
    position: absolute; left: 246px; top: 197px; width: 1.5px; height: 50px; background: var(--ink-soft);
  }
  .contact-list {
    position: absolute; left: 259px; top: 199px; list-style: none;
    font-size: 11.5px; line-height: 15px; color: var(--ink-soft);
  }
  .contact-list li { display: flex; align-items: center; gap: 9px; white-space: nowrap; }
  .contact-list svg { width: 11px; height: 11px; fill: var(--violet); flex: none; }
  .band-dark { position: absolute; left: 0; bottom: 0; width: 243px; height: 20px; background: var(--band-dark); }
  .band-violet { position: absolute; right: 0; bottom: 0; width: 209px; height: 20px; background: var(--violet); }

  /* Back face */
  .card-back { top: 470px; background: var(--card-dark); }
  .back-mark {
    position: absolute; left: 198px; top: 78px; width: 60px; height: 60px;
    border: 2px solid var(--violet-light);
  }
  .back-brand {
    position: absolute; left: 0; right: 0; top: 150px; text-align: center;
    font-family: "PT Sans", sans-serif; font-size: 17px; letter-spacing: 5px;
    color: var(--grey-mark); white-space: nowrap;
  }
  .back-rule { position: absolute; left: 70px; width: 310px; top: 177px; height: 1px; background: var(--grey-mark); }
  .lab-name {
    position: absolute; left: 0; right: 0; top: 183px; text-align: center;
    font-family: "PT Sans Narrow", sans-serif; font-size: 22px; color: var(--text-on-dark);
    letter-spacing: 0.2px; white-space: nowrap;
  }
</style>
</head>
<body>

<section class="card card-front" aria-label="Tarjeta, cara frontal">
  <div class="front-mark" aria-hidden="true"></div>
  <div class="front-brand">RM Tomás Rivera</div>
  <h1 class="holder-name">Tomás Rivera Ibarra</h1>
  <p class="holder-licence">M.P. 47203</p>

  <p class="holder-address">
    Técnico en Anatomía Patológica<br>
    Av. Paredes Luján 418 - 2do piso<br>
    Instituto Marbel, Córdoba, Argentina
  </p>
  <div class="contact-divider"></div>
  <ul class="contact-list">
    <li>
      <svg viewBox="0 0 24 24" aria-hidden="true"><path d="M6.6 10.8a15.1 15.1 0 0 0 6.6 6.6l2.2-2.2a1 1 0 0 1 1-.25 11.4 11.4 0 0 0 3.6.57 1 1 0 0 1 1 1V20a1 1 0 0 1-1 1A17 17 0 0 1 3 4a1 1 0 0 1 1-1h3.5a1 1 0 0 1 1 1c0 1.25.2 2.45.57 3.570a1 1 0 0 1-.25 1z"/></svg>
      (0351) 154820937
    </li>
    <li>
      <svg viewBox="0 0 24 24" aria-hidden="true"><path d="M2 5h20v14H2zm2 2v.5l8 5 8-5V7zm0 3v7h16v-7l-8 5z"/></svg>
      rivera.tomas@correolab.example
    </li>
    <li>
      <svg viewBox="0 0 24 24" aria-hidden="true"><path d="M12 2a10 10 0 1 0 0 20 10 10 0 0 0 0-20zm6.9 6h-2.9a15.7 15.7 0 0 0-1.4-3.6A8 8 0 0 1 18.9 8zM12 4c.8 1.2 1.5 2.5 1.9 4h-3.8c.4-1.500 1.1-2.8 1.9-4zM4.3 14a8 8 0 0 1 0-4h3.4a16 16 0 0 0 0 4zm.8 2h2.9c.3 1.3.8 2.5 1.4 3.6A8 8 0 0 1 5.1 16zM8 8H5.1a8 8 0 0 1 4.3-3.6C8.8 5.5 8.3 6.7 8 8zm4 12c-.8-1.2-1.5-2.5-1.9-4h3.8c-.4 1.5-1.1 2.8-1.9 4zm2.3-6H9.7a14.7 14.7 0 0 1 0-4h4.6a14.7 14.7 0 0 1 0 4zm.3 5.6c.6-1.1 1.1-2.3 1.4-3.6h2.9a8 8 0 0 1-4.3 3.6zm1.7-5.6a16 16 0 0 0 0-4h3.4a8 8 0 0 1 0 4z"/></svg>
      www.tomas-rivera.example
    </li>
  </ul>
  <div class="band-dark"></div>
  <div class="band-violet"></div>
</section>

<section class="card card-back" aria-label="Tarjeta, cara posterior">
  <div class="back-mark" aria-hidden="true"></div>
  <div class="back-brand">Tomás Rivera</div>
  <div class="back-rule"></div>
  <p class="lab-name">LABORATORIO DE PROCESAMIENTO HISTOLOGICO</p>
</section>

</body>
</html>
```